Tobelli Kids clothing needs two banners for its website

I have uploaded two images which are already 1767*887 in size, i want two website banners created using each image as a separate banner. I need the banners to be playful and with a lot of colors.
We sell kids clothes such as casual shirts, dresses, polo shirts, jeggings , jeans and cargo pants.
Our products are fashionable but with a unique twist. At the moment we are having 30% sale on all our Jackets.
We have just introduced our spring/summer 2014 collections with unique twist.
We also stock a lot of denim stuff too.
You can use the following messages on the banners: (or you come up with some similar messages)
1.)introducing our look sharp spring summer 2014 collection.
2.)30% Sale on all Jackets.
3.)Checkout our amazing unique styles: dresses, casual shirts, jeggings, pants, jeans ,cargo pants starting from $15
You can use the following messages on the banners:
PLease note: This project is for two separate banners, each image uploaded should be used for separate designs. Thank you
Kids and their parents
Clothing

```html
<!DOCTYPE html>
<html lang="en">
<head>
<meta charset="utf-8">
<title>Spring Summer 2014 Collection</title>
<link rel="stylesheet" href="https://fonts.googleapis.com/css2?family=Patrick+Hand&family=Indie+Flower&family=Fredoka:wght@600&display=swap">
<style>
  :root {
    --white: #ffffff;
    --red-orange: #f2460b;
    --orange: #f7941d;
    --sun-yellow: #f9e61f;
    --deep-yellow: #fbd40c;
    --pale-yellow: #fbef63;
    --teal: #4fe0e3;
    --olive: #4d4a12;
    --leaf: #5ccc1e;
    --mint: #8af28e;
    --violet: #e38cf5;
    --periwinkle: #8c8ef5;
    --pink: #ea1e73;
    --price-red: #ee2450;
    --ink: #3a3a3a;
    --denim: #5d7c9c;
    --khaki: #a89c83;
  }
  html, body {
    margin: 0;
    padding: 0;
    overflow: hidden;
    background: var(--white);
  }
  .banner {
    position: relative;
    width: 1200px;
    height: 602px;
    overflow: hidden;
    background: var(--white);
  }
  .backdrop {
    position: absolute;
    inset: 0;
  }
  .kids-photo {
    position: absolute;
    left: 10px;
    top: 40px;
    width: 470px;
    height: 562px;
  }
  .copy {
    position: absolute;
    margin: 0;
    white-space: nowrap;
    line-height: 1;
  }
  .intro {
    left: 760px; width: 440px; top: 40px;
    text-align: center;
    font: 30px "Patrick Hand", cursive;
    color: var(--white);
  }
  .season {
    left: 760px; width: 440px; top: 76px;
    text-align: center;
    font: 62px "Patrick Hand", cursive;
    color: var(--white);
    -webkit-text-stroke: 1.2px var(--white);
  }
  .collection {
    left: 760px; width: 440px; top: 154px;
    text-align: center;
    font: 50px "Patrick Hand", cursive;
    color: var(--sun-yellow);
    -webkit-text-stroke: 0.8px var(--sun-yellow);
  }
  .invite {
    left: 582px; top: 244px;
    font: 32px "Indie Flower", cursive;
    color: var(--pink);
    line-height: 48px;
  }
  .styles {
    left: 578px; top: 350px;
    font: 42px "Indie Flower", cursive;
    color: var(--ink);
    line-height: 70px;
    letter-spacing: -0.5px;
  }
  .price-line {
    left: 578px; top: 500px;
    font: 42px "Indie Flower", cursive;
    color: var(--ink);
    letter-spacing: -1.5px;
  }
  .price {
    font: 600 60px "Fredoka", sans-serif;
    color: var(--price-red);
    text-shadow: 2px 3px 0 rgba(120, 20, 30, 0.35);
    letter-spacing: 0;
    margin-left: 20px;
    vertical-align: -6px;
  }
</style>
</head>
<body>
<main class="banner">
  <svg class="backdrop" width="1200" height="602" viewBox="0 0 1200 602" aria-hidden="true">
    <defs>
      <filter id="soft" x="-50%" y="-50%" width="200%" height="200%">
        <feGaussianBlur stdDeviation="5"/>
      </filter>
      <clipPath id="clip-orange-top"><ellipse cx="265" cy="0" rx="125" ry="90"/></clipPath>
      <clipPath id="clip-red"><ellipse cx="990" cy="60" rx="240" ry="190"/></clipPath>
      <clipPath id="clip-orange-corner"><circle cx="1130" cy="650" r="140"/></clipPath>
    </defs>

    <ellipse cx="265" cy="0" rx="125" ry="90" fill="var(--red-orange)"/>
    <circle cx="175" cy="-10" r="70" fill="var(--teal)"/>
    <circle cx="175" cy="-10" r="70" fill="var(--olive)" clip-path="url(#clip-orange-top)"/>

    <circle cx="482" cy="50" r="50" fill="var(--teal)" filter="url(#soft)" opacity="0.95"/>
    <circle cx="205" cy="128" r="30" fill="var(--mint)" filter="url(#soft)"/>
    <circle cx="560" cy="202" r="34" fill="var(--violet)" filter="url(#soft)"/>
    <circle cx="180" cy="492" r="44" fill="var(--periwinkle)" filter="url(#soft)"/>

    <ellipse cx="1000" cy="560" rx="560" ry="470" fill="var(--sun-yellow)"/>
    <circle cx="900" cy="520" r="150" fill="var(--deep-yellow)"/>
    <circle cx="745" cy="265" r="38" fill="var(--pale-yellow)" opacity="0.8"/>
    <circle cx="1125" cy="300" r="78" fill="var(--pale-yellow)" opacity="0.85"/>
    <circle cx="500" cy="585" r="40" fill="var(--pale-yellow)" filter="url(#soft)"/>

    <ellipse cx="960" cy="90" rx="262" ry="205" fill="var(--orange)"/>
    <ellipse cx="990" cy="60" rx="240" ry="190" fill="var(--red-orange)"/>
    <circle cx="720" cy="-10" r="65" fill="var(--teal)"/>
    <circle cx="720" cy="-10" r="65" fill="var(--olive)" clip-path="url(#clip-red)"/>

    <circle cx="1130" cy="650" r="140" fill="var(--red-orange)"/>
    <circle cx="1210" cy="460" r="55" fill="var(--leaf)"/>
    <circle cx="1210" cy="460" r="55" fill="var(--olive)" clip-path="url(#clip-orange-corner)"/>
  </svg>

  <svg class="kids-photo" width="470" height="562" viewBox="0 0 470 562" role="img" aria-label="Photo of a smiling boy in a denim shirt and cargo pants and a girl in sunglasses, denim shirt, white jeggings and boots">
    <defs>
      <linearGradient id="photo-tones" x1="0" y1="0" x2="0" y2="1">
        <stop offset="0" stop-color="var(--denim)" stop-opacity="0.3"/>
        <stop offset="0.55" stop-color="var(--denim)" stop-opacity="0.25"/>
        <stop offset="1" stop-color="var(--khaki)" stop-opacity="0.3"/>
      </linearGradient>
    </defs>
    <rect width="470" height="562" rx="24" fill="url(#photo-tones)"/>
  </svg>

  <p class="copy intro">Introducing our look sharp</p>
  <h1 class="copy season">Spring Summer</h1>
  <p class="copy collection">2014 Collection</p>

  <p class="copy invite">Checkout our<br>Amazing Unique Styles:</p>
  <p class="copy styles">Dresses, Casual Shirts, Jeggings,<br>Pants, Jeans, Cargo Pants</p>
  <p class="copy price-line">Starting from<span class="price">$ 15</span></p>
</main>
</body>
</html>
```